Corwick Roof Company need Flier for Department of Tillage

We need a 2 page flier for distributing to Military Contractors and Department of Tillage. We install residential solar and this will be used for military base housing and other gov. projects on the residential home communities. We need to show how large of a company we are and how we are able to work with the military //gov. projects. Attached is our website and other marketing info for your use. Thanks and good luck!

Target Market(s)

Military and Government Contractors //Department of Tillage

Industry/Entity Type

Solar Energy

Requirements
Must have
• Our Why - Statement included

```html
<!DOCTYPE html>
<html lang="en">
<head>
<meta charset="utf-8">
<title>Brightfield Power – Two Page Flier</title>
<link href="https://fonts.googleapis.com/css2?family=Lato:wght@300;400;700;900&display=swap" rel="stylesheet">
<style>
  :root{
    --blue:#1485cc;
    --blue-dark:#0d6aa8;
    --green:#8cc63f;
    --green-dark:#6fae24;
    --ink:#2a2a2a;
    --footer:#2b2b2b;
    --paper:#f7f8f9;
    --stage:#ebe8e3;
  }
  html,body{margin:0;padding:0;width:1200px;height:926px;overflow:hidden;background:var(--stage);}
  body{font-family:"Lato",Arial,sans-serif;position:relative;}
  .page{position:absolute;top:67px;width:560px;height:791px;box-shadow:0 6px 18px rgba(0,0,0,.18);background:var(--paper);}
  .page--front{left:26px;}
  .page--back{left:614px;}
  .page svg{display:block;width:560px;height:791px;}
  text{font-family:"Lato",Arial,sans-serif;}
  .brand-name{fill:var(--blue);font-weight:700;}
  .title-light{fill:var(--ink);font-weight:300;font-size:38px;}
  .title-bold{fill:var(--blue);font-weight:900;font-size:80px;letter-spacing:-1px;}
  .pill-text{fill:#fff;font-weight:300;font-size:16px;}
  .pill-label{fill:#fff;font-weight:700;font-size:24px;letter-spacing:1px;}
  .tab-text{fill:#fff;font-weight:700;font-size:15px;}
  .footer-text{fill:#fff;font-size:10px;}
  .heading-blue{fill:var(--blue);font-weight:900;font-size:35px;}
  .heading-green{fill:var(--green);font-weight:900;font-size:24px;}
  .step-title{fill:var(--ink);font-weight:900;font-size:7.6px;}
  .step-text{fill:#444;font-size:7.2px;}
  .quote{fill:#333;font-size:9.3px;}
  .quote-name{fill:var(--green);font-size:9.3px;}
  .icon-line{fill:none;stroke:var(--blue);stroke-width:1.6;stroke-linecap:round;stroke-linejoin:round;}
</style>
</head>
<body>

<!-- Front page -->
<section class="page page--front">
<svg viewBox="0 0 598 845" xmlns="http://www.w3.org/2000/svg">
  <defs>
    <linearGradient id="bgPaper" x1="0" y1="0" x2="0" y2="1">
      <stop offset="0" stop-color="#eef0f2"/><stop offset="1" stop-color="#fafbfb"/>
    </linearGradient>
    <linearGradient id="panelPhoto" x1="0" y1="0" x2="1" y2="1">
      <stop offset="0" stop-color="#f4c27a"/><stop offset=".35" stop-color="#4a5f9a"/><stop offset="1" stop-color="#1c2a55"/>
    </linearGradient>
    <linearGradient id="housePhoto" x1="0" y1="0" x2="0" y2="1">
      <stop offset="0" stop-color="#c9d3dc"/><stop offset=".45" stop-color="#3a3f48"/><stop offset=".75" stop-color="#e7e3dc"/><stop offset="1" stop-color="#7a8a5a"/>
    </linearGradient>
    <linearGradient id="roofPhoto" x1="0" y1="0" x2="1" y2="1">
      <stop offset="0" stop-color="#2a8ad0"/><stop offset="1" stop-color="#0f4f86"/>
    </linearGradient>
    <linearGradient id="pillBlue" x1="0" y1="0" x2="0" y2="1">
      <stop offset="0" stop-color="#2b9be0"/><stop offset="1" stop-color="#0f6db0"/>
    </linearGradient>
  </defs>

  <rect class="paper" width="598" height="845" fill="url(#bgPaper)"/>

  <path role="img" aria-label="Photo of rooftop solar panels glowing in sunlight" d="M0,0 H240 C228,110 250,200 300,262 C200,275 100,278 0,285 Z" fill="url(#panelPhoto)"/>
  <path role="img" aria-label="Photo of a modern house with a solar panel roof" d="M286,0 H598 V210 C520,215 430,200 380,190 C330,150 300,90 286,0 Z" fill="url(#housePhoto)"/>
  <path role="img" aria-label="Photo of a blue solar roof with a wind turbine" d="M440,240 C500,225 560,205 598,195 V460 C540,430 480,390 440,350 Z" fill="url(#roofPhoto)"/>

  <path class="band-green" d="M240,0 C226,120 260,210 320,265" fill="none" stroke="var(--green)" stroke-width="8"/>
  <path class="band-blue" d="M0,270 C110,268 210,268 320,262" fill="none" stroke="var(--blue)" stroke-width="26"/>
  <path class="band-green" d="M0,292 C120,292 230,290 330,282" fill="none" stroke="var(--green)" stroke-width="5"/>
  <path class="band-blue" d="M440,235 C500,220 560,200 598,192" fill="none" stroke="var(--blue)" stroke-width="14"/>
  <path class="band-green" d="M410,360 C470,410 540,445 598,465" fill="none" stroke="var(--green)" stroke-width="6"/>
  <path class="band-blue" d="M400,372 C460,420 530,458 598,478" fill="none" stroke="var(--blue)" stroke-width="4"/>

  <g class="brand-badge">
    <circle cx="378" cy="282" r="92" fill="#fff" stroke="var(--green)" stroke-width="6"/>
    <text class="brand-name" x="378" y="280" text-anchor="middle" font-size="21">BRIGHTFIELD</text>
    <text class="brand-name" x="378" y="306" text-anchor="middle" font-size="21">POWER</text>
  </g>

  <text class="title-light" x="46" y="404">BRIGHTFIELD</text>
  <text class="title-bold" x="44" y="473">POWER</text>

  <g class="pill">
    <rect x="83" y="517" width="430" height="58" rx="29" fill="var(--green)"/>
    <path d="M378,517 H484 A29,29 0 0 1 484,575 H378 Z" fill="url(#pillBlue)"/>
    <text class="pill-text" x="100" y="541">The planet and your pocket book</text>
    <text class="pill-text" x="100" y="560">will thank you</text>
    <text class="pill-label" x="441" y="555" text-anchor="middle">WHY</text>
  </g>
  <g class="pill">
    <rect x="83" y="583" width="430" height="58" rx="29" fill="var(--green)"/>
    <path d="M378,583 H484 A29,29 0 0 1 484,641 H378 Z" fill="url(#pillBlue)"/>
    <text class="pill-text" x="100" y="607">Bringing the power and same</text>
    <text class="pill-text" x="100" y="626">to you</text>
    <text class="pill-label" x="441" y="620" text-anchor="middle">HOW</text>
  </g>
  <g class="pill">
    <rect x="83" y="649" width="430" height="58" rx="29" fill="var(--green)"/>
    <path d="M378,649 H484 A29,29 0 0 1 484,707 H378 Z" fill="url(#pillBlue)"/>
    <text class="pill-text" x="100" y="672">zero upfront cost power monthly</text>
    <text class="pill-text" x="100" y="691">energy costs</text>
    <text class="pill-label" x="441" y="686" text-anchor="middle">WHAT</text>
  </g>

  <g class="contact-tab">
    <rect x="0" y="783" width="598" height="9" fill="var(--green)"/>
    <path d="M200,762 H376 L398,792 H178 Z" fill="var(--blue)"/>
    <text class="tab-text" x="288" y="783" text-anchor="middle">CONTACT US</text>
  </g>
  <g class="footer">
    <rect x="0" y="792" width="598" height="53" fill="var(--footer)"/>
    <path d="M36,810 c0,4 4,8 8,8 l1.5,-1.5 -2,-2 -1.2,1 c-1.5,-.6 -2.6,-1.8 -3.2,-3.2 l1,-1.2 -2,-2 Z" fill="#fff"/>
    <text class="footer-text" x="53" y="818">(800) 555-0142</text>
    <rect x="163" y="811" width="8" height="6" fill="none" stroke="#fff" stroke-width="1"/>
    <path d="M163,811 l4,3.5 4,-3.5" fill="none" stroke="#fff" stroke-width="1"/>
    <text class="footer-text" x="178" y="818">hello@brightfieldpower.com</text>
    <path d="M353,819 c-3,-4 -4,-5.5 -4,-7 a4,4 0 0 1 8,0 c0,1.5 -1,3 -4,7 Z" fill="none" stroke="#fff" stroke-width="1"/>
    <text class="footer-text" x="361" y="818">58 Larkin Ave., Suite 210, Harrow NJ 08012</text>
  </g>
</svg>
</section>

<!-- Back page -->
<section class="page page--back">
<svg viewBox="0 0 598 845" xmlns="http://www.w3.org/2000/svg">
  <defs>
    <linearGradient id="bgPaper2" x1="0" y1="0" x2="0" y2="1">
      <stop offset="0" stop-color="#eef0f2"/><stop offset="1" stop-color="#fafbfb"/>
    </linearGradient>
    <linearGradient id="homePhoto" x1="0" y1="0" x2="0" y2="1">
      <stop offset="0" stop-color="#9fb8d4"/><stop offset=".35" stop-color="#b54a34"/><stop offset=".7" stop-color="#8a5a46"/><stop offset="1" stop-color="#6f9a3a"/>
    </linearGradient>
    <linearGradient id="iconRing" x1="0" y1="0" x2="1" y2="1">
      <stop offset="0" stop-color="var(--blue)"/><stop offset="1" stop-color="var(--green)"/>
    </linearGradient>
  </defs>

  <rect class="paper" width="598" height="845" fill="url(#bgPaper2)"/>

  <path role="img" aria-label="Photo of a brick family home with solar panels on a red roof, mountains behind" d="M0,0 H598 V215 C480,240 360,250 240,236 C150,228 70,200 0,172 Z" fill="url(#homePhoto)"/>
  <path class="band-green" d="M0,172 C70,200 150,228 240,236 C360,250 480,240 598,215" fill="none" stroke="var(--green)" stroke-width="12"/>
  <path class="band-blue" d="M150,240 C280,270 420,275 598,248 V312 C460,300 300,275 150,240 Z" fill="var(--blue)"/>

  <g class="brand-badge">
    <circle cx="108" cy="224" r="66" fill="#fff" stroke="var(--green)" stroke-width="5"/>
    <text class="brand-name" x="108" y="222" text-anchor="middle" font-size="15">BRIGHTFIELD</text>
    <text class="brand-name" x="108" y="241" text-anchor="middle" font-size="15">POWER</text>
  </g>

  <text class="heading-blue" x="36" y="366">We Make It Easy</text>

  <g class="steps">
    <circle cx="84" cy="440" r="31" fill="#fff" stroke="url(#iconRing)" stroke-width="2.5"/>
    <rect class="icon-line" x="70" y="428" width="22" height="16" rx="2"/>
    <path class="icon-line" d="M76,434 h10 M76,438 h7 M88,444 l4,6 v-6"/>
    <circle cx="111" cy="441" r="5" fill="var(--green)"/><text x="111" y="443.5" text-anchor="middle" font-size="6" fill="#fff">1</text>

    <path d="M133,440 h28 m-5,-4 l5,4 -5,4" fill="none" stroke="#777" stroke-width="1.2"/>

    <circle cx="222" cy="440" r="31" fill="#fff" stroke="url(#iconRing)" stroke-width="2.5"/>
    <path class="icon-line" d="M208,432 h24 l-4,14 h-24 Z M214,432 l-3,14 M220,432 l-3,14 M226,432 l-3,14 M207,439 h23 M218,446 v6 m-5,0 h10"/>
    <circle cx="222" cy="471" r="5" fill="var(--green)"/><text x="222" y="473.5" text-anchor="middle" font-size="6" fill="#fff">2</text>

    <path d="M274,440 h28 m-5,-4 l5,4 -5,4" fill="none" stroke="#777" stroke-width="1.2"/>

    <circle cx="363" cy="440" r="31" fill="#fff" stroke="url(#iconRing)" stroke-width="2.5"/>
    <rect class="icon-line" x="350" y="428" width="18" height="22" rx="2"/>
    <path class="icon-line" d="M354,434 h10 M354,439 h8"/>
    <circle class="icon-line" cx="369" cy="447" r="6"/>
    <path class="icon-line" d="M369,444 v3 h3"/>
    <circle cx="333" cy="440" r="5" fill="var(--green)"/><text x="333" y="442.5" text-anchor="middle" font-size="6" fill="#fff">3</text>

    <path d="M416,440 h28 m-5,-4 l5,4 -5,4" fill="none" stroke="#777" stroke-width="1.2"/>

    <circle cx="505" cy="440" r="31" fill="#fff" stroke="url(#iconRing)" stroke-width="2.5"/>
    <circle cx="505" cy="437" r="8" fill="none" stroke="var(--green)" stroke-width="1.8"/>
    <path d="M501,447 h8 M502,451 h6 M505,424 v-4 M494,428 l-3,-3 M516,428 l3,-3" fill="none" stroke="var(--green)" stroke-width="1.8" stroke-linecap="round"/>
    <circle cx="505" cy="409" r="5" fill="var(--green)"/><text x="505" y="411.5" text-anchor="middle" font-size="6" fill="#fff">4</text>

    <text class="step-title" x="14" y="490">Speak To A Solar Consultant</text>
    <text class="step-text" x="14" y="499">Meet with one of our energy consultants</text>
    <text class="step-text" x="14" y="508">to review your solar options.</text>

    <text class="step-title" x="170" y="490">We'll Design Your Solar Panel</text>
    <text class="step-title" x="170" y="499">System</text>
    <text class="step-text" x="170" y="508">We'll finalize the details for tip</text>
    <text class="step-text" x="170" y="517">top accuracy.</text>

    <text class="step-title" x="304" y="490">Schedule Your 1 Day Install</text>
    <text class="step-text" x="304" y="499">Let us do the heavy lifting as you</text>
    <text class="step-text" x="304" y="508">watch your home upgrade to solar.</text>

    <text class="step-title" x="440" y="490">Start Saving On Your Electricity Bill</text>
    <text class="step-text" x="440" y="499">Watch your electric bill lower and your</text>
    <text class="step-text" x="440" y="508">energy savings build for year to come.</text>
  </g>

  <text class="heading-green" x="31" y="582">What People Are Saying</text>

  <g class="testimonials">
    <text class="quote" x="31" y="619">My husband and I decided to go solar after 3 of our</text>
    <text class="quote" x="31" y="631">neighbors did. After having it I don't know why we</text>
    <text class="quote" x="31" y="643">waited so long!</text>
    <text class="quote-name" x="31" y="667">RENEE K</text>

    <text class="quote" x="31" y="691">We were a bit nervous to go solar.. after our consulta-</text>
    <text class="quote" x="31" y="703">tion with Sam it was very easy to see that solar was our</text>
    <text class="quote" x="31" y="715">best option. Now we are saving tons on our electric</text>
    <text class="quote" x="31" y="727">bill! Thanks !</text>
    <text class="quote-name" x="31" y="751">WALT AND NORA B.</text>

    <text class="quote" x="295" y="619">I had met with a few different companies and didn't care for their</text>
    <text class="quote" x="295" y="631">options. Brightfield had an option we liked and we went for it! Its</text>
    <text class="quote" x="295" y="643">been working great for us.</text>
    <text class="quote-name" x="295" y="667">MARCUS AND ELENA P</text>
  </g>

  <g class="contact-tab">
    <rect x="0" y="773" width="598" height="9" fill="var(--green)"/>
    <path d="M202,752 H352 L374,782 H180 Z" fill="var(--blue)"/>
    <text class="tab-text" x="277" y="772" text-anchor="middle">CONTACT US</text>
  </g>
  <g class="footer">
    <rect x="0" y="782" width="598" height="63" fill="var(--footer)"/>
    <path d="M33,814 c0,4 4,8 8,8 l1.5,-1.5 -2,-2 -1.2,1 c-1.5,-.6 -2.6,-1.8 -3.2,-3.2 l1,-1.2 -2,-2 Z" fill="#fff"/>
    <text class="footer-text" x="52" y="822">(800) 555-0142</text>
    <rect x="162" y="815" width="8" height="6" fill="none" stroke="#fff" stroke-width="1"/>
    <path d="M162,815 l4,3.5 4,-3.5" fill="none" stroke="#fff" stroke-width="1"/>
    <text class="footer-text" x="177" y="822">hello@brightfieldpower.com</text>
    <path d="M351,823 c-3,-4 -4,-5.5 -4,-7 a4,4 0 0 1 8,0 c0,1.5 -1,3 -4,7 Z" fill="none" stroke="#fff" stroke-width="1"/>
    <text class="footer-text" x="359" y="822">58 Larkin Ave., Suite 210, Harrow NJ 08012</text>
  </g>
</svg>
</section>

</body>
</html>
```